Strategic Plan Notecards (4.25in x 5.5 in)

I need a design for project cards that will be handed out to the general public as part of a Strategic Planning effort for a client. I'd like the cards to be 4.25 x 5.5 so that they can be printed 4 to a US letter-size sheet of paper.

The Project title is "City of Fieldhaven Strategic Plan Update"
Needs to include text:

For more info, go to www.plainsfutureplan.org
Take the Vision Survey at http://tnyurl.example/FieldhavenIdeas
What do YOU want Fieldhaven to be?

Other variations on this text will be considered.

Target Market(s)

General Public

Font styles to use
Serif
Sans Serif

Colors

Designer to choose colors to be used in the design.

Requirements
Must have
• An interesting and fun visual appeal. Nothing stuffy. Should have a bright graphic background and interesting typefaces for the text.
Nice to have
• One of the biggest assets in the community is the Missouri River - some depiction of a river would be great.

```html
<!DOCTYPE html>
<html lang="en">
<head>
<meta charset="utf-8">
<title>Fieldhaven Strategic Plan Update</title>
<link rel="stylesheet" href="https://fonts.googleapis.com/css2?family=Montserrat:wght@400;500;600;700;800&display=swap">
<style>
  :root {
    --navy: #14105a;
    --cyan: #0aaee8;
    --white: #ffffff;
    --ink: #14105a;
    --page: #9a9a9a;
    --sky-top: #7fa9d6;
    --sky-bottom: #b9cbe0;
    --river: #8c7d67;
  }
  * { box-sizing: border-box; margin: 0; padding: 0; }
  html, body { width: 1200px; height: 1200px; overflow: hidden; }
  body {
    background: var(--page);
    font-family: "Montserrat", sans-serif;
    position: relative;
  }
  .card {
    position: absolute;
    left: 150px; top: 18px;
    width: 900px; height: 1165px;
    background: var(--white);
    overflow: hidden;
  }
  .hero-photo {
    position: absolute; left: 0; top: 0; width: 900px; height: 552px;
    background: linear-gradient(180deg, var(--sky-top) 0%, var(--sky-bottom) 55%, #6e7a52 62%, var(--river) 75%, #5c5446 100%);
  }
  .logo-panel { position: absolute; left: 0; top: 0; }
  .logo-name {
    position: absolute; left: 560px; top: 100px;
    font-size: 58px; font-weight: 700; color: var(--navy);
    letter-spacing: -1px;
  }
  .title-band { position: absolute; left: 0; top: 545px; }
  .title {
    position: absolute; left: 55px; top: 558px;
    font-size: 57px; font-weight: 800; line-height: 60px;
    color: var(--white); letter-spacing: -1.5px;
  }
  .title .accent { color: var(--cyan); }
  .intro {
    position: absolute; left: 53px; top: 700px; width: 794px;
    font-size: 24.5px; line-height: 32.5px; color: var(--ink);
    text-align: justify; font-weight: 400;
  }
  .intro strong { font-weight: 700; }
  .survey {
    position: absolute; left: 52px; top: 882px;
    display: flex; align-items: center; gap: 12px;
  }
  .survey-text { color: var(--ink); font-weight: 600; }
  .survey-text .lead { font-size: 30px; line-height: 38px; }
  .survey-text .lead em { font-style: normal; color: var(--cyan); font-weight: 500; }
  .survey-text .url { font-size: 21px; font-weight: 700; line-height: 34px; }
  .prompt-band {
    position: absolute; left: 0; top: 967px; width: 900px; height: 43px;
    background: var(--cyan);
    padding-left: 54px;
    font-size: 21px; line-height: 43px; color: var(--white); font-weight: 500;
  }
  .prompt-band strong { color: var(--navy); font-weight: 800; font-size: 26px; }
  .footer {
    position: absolute; left: 0; top: 1010px; width: 900px; height: 155px;
    background: var(--navy);
  }
  .contacts {
    position: absolute; left: 53px; top: 1020px; list-style: none;
    color: var(--white); font-size: 26px; line-height: 33px;
  }
  .contacts li { display: flex; align-items: center; gap: 8px; }
  .contacts .bold { font-weight: 700; }
  .device-photo {
    position: absolute; left: 592px; top: 840px;
    width: 272px; height: 272px; border-radius: 50%;
    border: 8px solid var(--white);
    background: radial-gradient(circle at 45% 45%, #e9e9e9 0%, #c8c8c8 35%, #2a2a2a 60%, #b58a5e 100%);
  }
</style>
</head>
<body>
  <main class="card">
    <div class="hero-photo" role="img" aria-label="Photo of a steel truss railroad bridge over the Missouri River with trees on the banks"></div>

    <svg class="logo-panel" width="900" height="210" viewBox="0 0 900 210" aria-hidden="true">
      <path d="M422 0 H900 V203 H570 C530 203 520 180 500 140 L422 0 Z" fill="#ffffff"/>
    </svg>
    <div class="logo-name">Fieldhaven</div>

    <svg class="title-band" width="900" height="145" viewBox="0 0 900 145" aria-hidden="true">
      <path d="M0 0 H845 L780 100 C760 130 740 142 700 142 H0 Z" fill="#14105a"/>
    </svg>
    <h1 class="title">FIELDHAVEN <span class="accent">STRATEGIC</span><br><span class="accent">PLAN</span> UPDATE</h1>

    <p class="intro"><strong>Be bold.</strong> Share your best ideas. Help shape the future by spending about <strong>15 minutes taking a survey that asks you to open up about what you hope Fieldhaven will be in the next two decades</strong>. No idea is off the table for discussion, so now is the time to let us know what YOU think.</p>

    <div class="survey">
      <svg width="72" height="72" viewBox="0 0 72 72" aria-hidden="true">
        <g fill="none" stroke="#0aaee8" stroke-width="3.5">
          <circle cx="34" cy="34" r="31"/>
          <ellipse cx="34" cy="34" rx="14" ry="31"/>
          <line x1="34" y1="3" x2="34" y2="65"/>
          <line x1="4" y1="24" x2="64" y2="24"/>
          <line x1="4" y1="44" x2="64" y2="44"/>
        </g>
        <path d="M40 40 L68 52 L57 55 L66 66 L61 70 L52 59 L46 66 Z" fill="#0aaee8" stroke="#fff" stroke-width="2"/>
      </svg>
      <div class="survey-text">
        <div class="lead">Take the <em>Vision Survey</em> at</div>
        <div class="url">http://tnyurl.example/FieldhavenIdeas</div>
      </div>
    </div>

    <div class="prompt-band">WHAT DO YOU WANT <strong>FIELDHAVEN <span style="color:#fff">TO</span> BE</strong>?</div>

    <div class="footer"></div>
    <ul class="contacts">
      <li>
        <svg width="26" height="26" viewBox="0 0 26 26" aria-hidden="true"><circle cx="13" cy="13" r="11.5" fill="none" stroke="#0aaee8" stroke-width="1.8"/><path d="M9 7 l2.5 3 -1.5 1.5 c1 2 2.5 3.5 4.5 4.5 l1.5 -1.5 3 2.5 -1.5 2 c-5 0 -10 -5 -10 -10 Z" fill="#0aaee8"/></svg>
        <span class="bold">555-014-2290</span>
      </li>
      <li>
        <svg width="26" height="26" viewBox="0 0 26 26" aria-hidden="true"><circle cx="13" cy="13" r="11.5" fill="none" stroke="#0aaee8" stroke-width="1.8"/><path d="M10 7 L18 15 L14 15 L16 19 L14 20 L12 16 L10 18 Z" fill="#0aaee8"/></svg>
        <span>www.<span class="bold">plainsfutureplan</span>.org</span>
      </li>
      <li>
        <svg width="26" height="26" viewBox="0 0 26 26" aria-hidden="true"><circle cx="13" cy="13" r="11.5" fill="none" stroke="#0aaee8" stroke-width="1.8"/><rect x="7" y="9" width="12" height="9" fill="none" stroke="#0aaee8" stroke-width="1.6"/><path d="M7 9 L13 14 L19 9" fill="none" stroke="#0aaee8" stroke-width="1.6"/></svg>
        <span>hello@fieldhavenplanning.example</span>
      </li>
    </ul>

    <div class="device-photo" role="img" aria-label="Photo of hands holding a tablet showing the online vision survey page"></div>
  </main>
</body>
</html>
```